Thornwell Building Company - advertisement poster

I am looking to print some canvas signs to advertise my general contracting company, Thornwell Building Company. The sign will measure 6' long x 3' high so the size should match that ratio. I already have a logo icon, which is the Letter 'A' and some trees that I would like to incorporate, see attached. I would also like the to have the following information listed:
1) phone number: 472-318-6095
2) email: thornwellbuildingcompany@mailvistra.net
3) website: thornwellbuildingcompany.com
4) Lic#5386204
5) I want to use this text: "BUILD WITH THE T-CREW!"

The ad should be relatively simple and clean. Black and Green are my company colors. I am open to creative ideas!

Target Market(s)

People looking to renovate their homes

Industry/Entity Type

Construction

Colors
59FF00
82FF00
B8FF75
E3FFCB
F4FFEA

Requirements
Must have
• Must have my company logo
Should not have
• No photos or complex graphics

```html
<!DOCTYPE html>
<html lang="en">
<head>
<meta charset="utf-8">
<title>Thornwell Building Company – Sign</title>
<link href="https://fonts.googleapis.com/css2?family=Barlow:wght@400;500;700&family=Michroma&display=swap" rel="stylesheet">
<style>
  :root{
    --ink:#000000;
    --paper:#ffffff;
    --stage:#e6e7e8;
    --green:#6db33f;
    --green-light:#8bc265;
    --green-dark:#5a9c34;
    --grey-1:#bcbec0;
    --grey-2:#9a9c9e;
    --grey-3:#77797b;
    --grey-4:#58595b;
    --text-dark:#111111;
  }
  *{margin:0;padding:0;box-sizing:border-box}
  html,body{width:1093px;height:1200px;overflow:hidden;background:var(--stage)}
  .sign{
    position:absolute;left:0;top:327px;width:1093px;height:546px;
    background:var(--paper);overflow:hidden;
    font-family:"Barlow",Arial,sans-serif;
  }
  .sign__shapes{position:absolute;inset:0}
  .headline{position:absolute;left:30px;top:40px;line-height:1}
  .headline__lead{display:block;font-size:60px;font-weight:400;color:var(--text-dark);letter-spacing:0.5px}
  .headline__punch{display:block;font-size:110px;font-weight:700;color:var(--green);margin-top:-2px;letter-spacing:-1px}
  .license{position:absolute;left:33px;bottom:38px;font-size:17px;font-weight:500;letter-spacing:1.5px;color:var(--text-dark)}
  .brand{position:absolute;left:660px;top:175px;width:410px;text-align:center;color:var(--paper);font-family:"Michroma",sans-serif}
  .brand__row{display:flex;align-items:center;justify-content:space-between;margin-bottom:26px}
  .brand__estd{font-size:12px;letter-spacing:4px;padding:5px 0;border-top:1px solid var(--green);border-bottom:1px solid var(--green)}
  .brand__mark{width:60px;height:60px;background:var(--green)}
  .brand__name{font-size:34px;letter-spacing:1px;line-height:1.1}
  .brand__sub{font-size:15px;letter-spacing:7px;margin-top:8px}
  .contact{position:absolute;right:40px;bottom:22px;list-style:none;text-align:right;color:var(--paper)}
  .contact__item{display:flex;align-items:center;justify-content:flex-end;gap:18px;height:38px;font-size:23px;font-weight:500;letter-spacing:1.8px}
  .contact__icon{width:20px;height:20px;flex:none}
</style>
</head>
<body>
<main class="sign">
  <svg class="sign__shapes" viewBox="0 0 1093 546" aria-hidden="true">
    <polygon points="752,0 1093,0 1093,546 370,546 660,112" fill="var(--ink)"/>
    <polygon points="640,0 752,0 660,112 380,420" fill="var(--green)"/>
    <polygon points="665,0 752,0 660,112 420,380" fill="var(--green-light)"/>
    <polygon points="710,0 752,0 660,112 560,230" fill="var(--green-dark)"/>
    <polygon points="660,112 250,546 295,546" fill="var(--grey-4)"/>
    <polygon points="660,112 295,546 325,546" fill="var(--grey-3)"/>
    <polygon points="660,112 325,546 350,546" fill="var(--grey-2)"/>
    <polygon points="660,112 350,546 370,546" fill="var(--grey-1)"/>
    <polygon points="1010,0 1093,0 1093,85" fill="var(--green)"/>
  </svg>

  <h1 class="headline">
    <span class="headline__lead">BUILD WITH THE</span>
    <span class="headline__punch">T-CREW!</span>
  </h1>

  <p class="license">License # 5386204</p>

  <div class="brand">
    <div class="brand__row">
      <span class="brand__estd">ESTD</span>
      <span class="brand__mark"></span>
      <span class="brand__estd">2020</span>
    </div>
    <div class="brand__name">THORNWELL</div>
    <div class="brand__sub">BUILDING COMPANY</div>
  </div>

  <ul class="contact">
    <li class="contact__item">472-318-6095
      <svg class="contact__icon" viewBox="0 0 24 24" fill="none" stroke="var(--green)" stroke-width="1.6"><path d="M5 3h4l2 5-3 2a11 11 0 0 0 6 6l2-3 5 2v4a2 2 0 0 1-2 2A17 17 0 0 1 3 5a2 2 0 0 1 2-2z"/></svg>
    </li>
    <li class="contact__item">thornwellbuildingcompany@mailvistra.net
      <svg class="contact__icon" viewBox="0 0 24 24" fill="none" stroke="var(--green)" stroke-width="1.6"><rect x="3" y="5" width="18" height="14"/><path d="M3 5l9 8 9-8M3 19l7-7M21 19l-7-7"/></svg>
    </li>
    <li class="contact__item">www.thornwellbuildingcompany.com
      <svg class="contact__icon" viewBox="0 0 24 24" fill="none" stroke="var(--green)" stroke-width="1.6"><circle cx="12" cy="12" r="9"/><ellipse cx="12" cy="12" rx="4" ry="9"/><path d="M3 12h18M5 7h14M5 17h14"/></svg>
    </li>
  </ul>
</main>
</body>
</html>
```